TAMBRIX passionate and energetic Business Card

We need a business card design for a new company based in Melbourne called "TAMBRIX" www.tambrix.com.au. We delivery food to the customer, we got 80+ restaurant at the moment. We would like to see designs that use the color red pearl white. The final design should be looks passionate and energetic. Should be related to the website www.tambrix.com.au

Target Market(s)

18-55 AGE

Industry/Entity Type

Business

Contact Information for Business Card

Fast Easy way to get food order on the internet.

Font styles to use
Serif
Sans Serif
Decorative

Colors
ec1f27
fff5ef

Requirements
Must have
• Should relative to the website www.tambrix.com.au
Nice to have
• No Idea
Should not have
• No Idea

```html
<!DOCTYPE html>
<html lang="en">
<head>
<meta charset="utf-8">
<title>TAMBRIX Business Card</title>
<link rel="stylesheet" href="https://fonts.googleapis.com/css2?family=Open+Sans:ital,wght@0,400;0,700&family=Noto+Sans+SC:wght@500&family=Pinyon+Script&display=swap">
<style>
  :root {
    --red: #ec1f27;
    --deep-red: #b8151b;
    --pearl: #fff5ef;
    --card: #f4efe6;
    --ink: #1c1c1c;
    --black: #121212;
    --backdrop: #d9d9d9;
  }
  * { box-sizing: border-box; margin: 0; padding: 0; }
  html, body { width: 1200px; height: 852px; overflow: hidden; }
  body {
    background: var(--backdrop);
    font-family: "Open Sans", Arial, sans-serif;
    position: relative;
  }
  .card {
    position: absolute;
    width: 540px;
    height: 310px;
    border-radius: 22px;
    background: var(--card);
    overflow: hidden;
    box-shadow: 0 10px 24px rgba(0,0,0,0.22);
  }
  .card--front { left: 80px; top: 70px; }
  .card--back { left: 580px; top: 460px; }

  .tagline {
    font-family: "Noto Sans SC", sans-serif;
    font-weight: 500;
    color: var(--ink);
    letter-spacing: 1px;
  }
  .brand-name {
    font-family: "Open Sans", Arial, sans-serif;
    font-weight: 700;
    color: var(--red);
    letter-spacing: 2px;
    line-height: 1;
  }

  .card--front .brand { position: absolute; left: 0; right: 0; top: 112px; text-align: center; }
  .card--front .tagline { font-size: 16px; margin-bottom: 8px; }
  .card--front .brand-name { font-size: 58px; }

  .photo { position: absolute; }
  .photo--tomatoes-front {
    right: 0; top: 0; width: 170px; height: 90px;
    background: radial-gradient(ellipse at 70% 30%, #d4261c 0%, #e0473a 40%, rgba(244,239,230,0) 72%);
  }
  .photo--chillies {
    left: 0; bottom: 0; width: 130px; height: 120px;
    background: radial-gradient(circle at 35% 70%, #b5201a 0%, #8a4a2a 45%, rgba(244,239,230,0) 72%);
  }
  .photo--tomatoes-back {
    right: 0; top: 0; width: 150px; height: 60px;
    background: radial-gradient(ellipse at 65% 35%, #d4261c 0%, #e0473a 40%, rgba(244,239,230,0) 72%);
  }

  .card--back .waves { position: absolute; inset: 0; width: 540px; height: 310px; }
  .card--back .brand { position: absolute; left: 36px; top: 54px; }
  .card--back .tagline { font-size: 17px; margin: 0 0 6px 80px; }
  .card--back .brand-name { font-size: 54px; }

  .person { position: absolute; left: 68px; top: 192px; }
  .person-name { font-family: "Pinyon Script", cursive; font-size: 30px; color: var(--ink); }
  .person-title { font-size: 11px; color: var(--ink); margin-left: 14px; margin-top: -2px; }

  .contact {
    position: absolute; right: 18px; top: 162px;
    list-style: none; text-align: right; color: var(--pearl);
    font-size: 11px; line-height: 19px;
  }
  .contact li { display: flex; justify-content: flex-end; align-items: center; gap: 7px; white-space: nowrap; }
  .contact svg { width: 10px; height: 10px; fill: var(--red); flex: none; }
</style>
</head>
<body>

<section class="card card--front" aria-label="Business card front">
  <div class="photo photo--tomatoes-front" role="img" aria-label="Photo of fresh red tomatoes"></div>
  <div class="brand">
    <p class="tagline">保温配送 风雨无阻</p>
    <p class="brand-name">TAMBRIX</p>
  </div>
  <div class="photo photo--chillies" role="img" aria-label="Photo of a wooden bowl of red chillies"></div>
</section>

<section class="card card--back" aria-label="Business card back">
  <div class="photo photo--tomatoes-back" role="img" aria-label="Photo of fresh red tomatoes"></div>
  <svg class="waves" viewBox="0 0 540 310" aria-hidden="true">
    <path d="M540 55 C440 70 380 110 350 165 C325 210 305 255 270 290 C260 300 250 306 240 310 L540 310 Z" fill="var(--black)"/>
    <path d="M540 44 C430 60 368 104 338 160 C312 210 292 258 255 290 C225 312 160 300 70 300" fill="none" stroke="var(--red)" stroke-width="4"/>
    <path d="M530 52 C428 70 372 112 344 166 C318 214 298 258 262 290 C232 308 170 298 110 296" fill="none" stroke="var(--deep-red)" stroke-width="1.5"/>
    <path d="M0 292 C100 300 180 298 240 292 L228 310 L0 310 Z" fill="var(--red)"/>
  </svg>

  <div class="brand">
    <p class="tagline">保温配送 风雨无阻</p>
    <p class="brand-name">TAMBRIX</p>
  </div>

  <div class="person">
    <p class="person-name">Your Name</p>
    <p class="person-title">Title</p>
  </div>

  <ul class="contact">
    <li>www.tambrix.com.au
      <svg viewBox="0 0 12 12"><circle cx="6" cy="6" r="5.5" fill="none" stroke="var(--red)" stroke-width="1.2"/><path d="M0.5 6h11M6 0.5c-3 3-3 8 0 11M6 0.5c3 3 3 8 0 11" fill="none" stroke="var(--red)" stroke-width="1"/></svg>
    </li>
    <li>admin@tambrix.com.au
      <svg viewBox="0 0 12 12"><rect x="0.5" y="2" width="11" height="8" rx="1"/><path d="M1 2.5l5 4 5-4" fill="none" stroke="var(--black)" stroke-width="1"/></svg>
    </li>
    <li>03 9555 0148 , 0400 555 219
      <svg viewBox="0 0 12 12"><path d="M2.5 0.8l2 2.4-1.2 1.4c.8 1.7 2 2.9 3.7 3.7l1.4-1.2 2.4 2-1.3 2C5.2 10.8 1.2 6.8 0.5 2z"/></svg>
    </li>
    <li>1204/88 Harlow St, Melbourne, 3000
      <svg viewBox="0 0 12 12"><path d="M6 0.5a4 4 0 0 1 4 4c0 3-4 7-4 7s-4-4-4-7a4 4 0 0 1 4-4z"/><circle cx="6" cy="4.5" r="1.5" fill="var(--black)"/></svg>
    </li>
  </ul>
</section>

</body>
</html>
```